Magazine Cover & Back, Course Overview

Please read this whole description and follow directions before proceeding. Please do not submit multiple designs that look similar. If you submit multiple designs that look similar you will be disqualified and receive a poor rating. A magazine design includes a cover and back. This is a single design and should be submitted as such. Do not submit one design for the front only, then a separate design for the back, then a third mock up. Submit all as a single design. I need a magazine cover and back. The size will be standard paper size, 8-1/2" x 11". It will be used for a course overview, a summary of a boating instruction course. I have attached examples and pictures that can be used. I have also attached required content. The final designs must NOT be AI files. Text must be editable with Adobe Acrobat DC.

Target Market(s)

Military & Government

Industry/Entity Type

Military & Government

Requirements
Must have
• See attached.
Nice to have
• See attached.
Should not have
• See attached.

```html
<!DOCTYPE html>
<html lang="en">
<head>
<meta charset="utf-8">
<title>Diver Support Vessel Training – Course Overview</title>
<link rel="stylesheet" href="https://fonts.googleapis.com/css2?family=Open+Sans:wght@400;600;700;800&display=swap">
<style>
  :root{
    --bg:#e3e7ee;
    --page:#ffffff;
    --frame:#6f7073;
    --ink:#333333;
    --ink-dark:#111111;
    --gold:#d6a91c;
    --brand:#4d5566;
    --faint:#d9d6cc;
  }
  *{box-sizing:border-box;margin:0;padding:0}
  html,body{width:1200px;height:1000px;overflow:hidden}
  body{background:var(--bg);font-family:"Open Sans",Arial,sans-serif;color:var(--ink)}
  .spread{position:absolute;left:143px;top:215px;display:flex;gap:34px}
  .page{position:relative;width:440px;height:570px;background:var(--page);box-shadow:0 1px 4px rgba(0,0,0,.08)}
  .frame{position:absolute;inset:18px;border:1px solid var(--frame);outline:1px solid var(--frame);outline-offset:-5px}
  .frame::before,.frame::after{content:"";position:absolute;width:10px;height:10px;border:1px solid var(--frame)}
  .frame::before{top:-6px;left:-6px;border-right:none;border-bottom:none}
  .frame::after{bottom:-6px;right:-6px;border-left:none;border-top:none}

  .brand-foot{position:absolute;left:0;right:0;bottom:40px;display:flex;justify-content:center;align-items:center;gap:6px;font-size:15px;font-weight:600;color:var(--brand)}
  .brand-foot .dot{width:12px;height:12px;border:1.5px solid var(--brand);border-radius:50%}

  /* back */
  .seal{position:absolute;left:50%;top:205px;transform:translateX(-50%);width:180px;height:180px;border-radius:50%;border:6px solid var(--faint);display:flex;align-items:center;justify-content:center;text-align:center}
  .seal-name{font-size:17px;font-weight:800;color:var(--faint);line-height:1.2;text-transform:uppercase;width:130px}

  /* cover */
  .cover-head{position:absolute;left:28px;top:30px;display:flex;align-items:center;gap:10px}
  .cover-head .mark{width:62px;height:62px;border-radius:50%;background:#151515;border:3px solid var(--gold)}
  .cover-head .firm{font-size:9px;font-weight:700;letter-spacing:.5px;text-transform:uppercase;color:var(--brand)}
  .cover-title{font-size:19px;font-weight:700;color:var(--ink)}
  .tiles{position:absolute;left:32px;right:32px;top:102px;display:flex;gap:5px}
  .tile{flex:1;background:var(--gold)}
  .tile .shot{height:76px}
  .tile p{font-size:8.5px;font-weight:700;color:var(--ink-dark);line-height:1.15;padding:3px 4px 4px;height:34px}
  .shot-a{background:linear-gradient(135deg,#8b9aa5,#5d6a55 60%,#c9c2b4)}
  .shot-b{background:linear-gradient(180deg,#c8ccd0,#707a82 55%,#9aa0a5)}
  .shot-c{background:linear-gradient(90deg,#2a2d30 30%,#8a9fb0 60%,#c7ccd0)}
  .hero{position:absolute;left:24px;right:24px;top:212px;height:340px;
    background:linear-gradient(180deg,#d4d9dc 0%,#a9b3b9 18%,#5e88a8 30%,#98a3aa 40%,#8e979d 60%,#b9c0c6 78%,#ffffff 96%)}
  .pill{position:absolute;left:50%;top:404px;transform:translateX(-50%);background:var(--gold);border-radius:14px;padding:5px 20px;font-size:12.5px;font-weight:700;color:var(--ink-dark);white-space:nowrap}
  .claim{position:absolute;left:50px;right:50px;top:443px;border:1px solid var(--ink);outline:1px solid var(--ink);outline-offset:-4px;padding:6px 10px;text-align:center;font-size:11.5px;font-weight:700;line-height:1.3;color:var(--ink-dark)}
</style>
</head>
<body>
<main class="spread">
  <section class="page back-cover">
    <div class="frame"></div>
    <div class="seal"><span class="seal-name">Harbor Point Boat Training</span></div>
    <div class="brand-foot"><span class="dot"></span>Keelwright</div>
  </section>

  <section class="page front-cover">
    <div class="frame"></div>
    <div class="hero" role="img" aria-label="Sailor standing on the deck of a grey diver support vessel on open water"></div>
    <header class="cover-head">
      <span class="mark"></span>
      <div>
        <div class="firm">Harbor Point Boat Training</div>
        <h1 class="cover-title">Diver Support Vessel Training</h1>
      </div>
    </header>
    <div class="tiles">
      <figure class="tile"><div class="shot shot-a" role="img" aria-label="Instructor guiding a sailor at the helm"></div><p>To assist Navy Sailors with Becoming More Proficient Coxswains</p></figure>
      <figure class="tile"><div class="shot shot-b" role="img" aria-label="Vessel control console"></div><p>Focused on Safety &amp; Close-Quarters Maneuvering</p></figure>
      <figure class="tile"><div class="shot shot-c" role="img" aria-label="Boat captain on deck at the pier"></div><p>Taught by Reputable USCG Licensed Boat Captains</p></figure>
    </div>
    <div class="pill">Includes Useful Aids</div>
    <div class="claim">Custom Made Course for Specific Users,<br>Scenarios and Vessels Based on OIC Involvement,<br>Client Feedback and After Action Reviews</div>
    <div class="brand-foot"><span class="dot"></span>Keelwright</div>
  </section>
</main>
</body>
</html>
```